Business cards, stationery and report cover
For market research and marketing company in New Zealand
Simple
Rosalind Thorpe
Level 1
57 Pemberly Road
Milford
Auckland
PO Box 46-582
Auckland 0963
rosalind@lumenvex.co.nz
www.lumenvex.co.nz
From this process we are looking for business cards, letterhead, comp slip, as well as a generic cover page and inside page for our reports (e.g heading styles, footers etc). Both report pages need to be easily replicated or applied to Microsoft Word reports. We are PC users if this makes a difference.
The information for the business cards can be on the front or the back - depending on your design and what looks best. Most people would contact us by phone/cell/email.
We would like to be viewed as professional, competent, modern and well established. We don't want to look like we are an advertising agency, or quirky or too different from our competitors. However, we'd like to be eye catching and interesting! Our typical clients are intelligent managers who are over 35 years and a mixture of male and female.
Please let us know if you have any questions or would like clarification on anything.
As noted in 'Additional Comments' you can choose what details would look best on the front of the business card, and which you would recommend going on the back of the card.
This is our new logo.

```html
<!DOCTYPE html>
<html lang="en">
<head>
<meta charset="utf-8">
<title>lumenvex stationery set</title>
<link href="https://fonts.googleapis.com/css2?family=Open+Sans:wght@300;400;600&display=swap" rel="stylesheet">
<style>
:root{
  --bg:#e9e6e1;
  --paper:#ffffff;
  --brand-blue:#1f6fc1;
  --brand-blue-light:#5a9bdc;
  --ink:#4a5058;
  --ink-soft:#8a9099;
  --charcoal:#3a3b3d;
  --charcoal-dark:#262729;
  --label:#3b2a1c;
}
*{box-sizing:border-box;margin:0;padding:0}
html,body{width:1200px;height:1025px;overflow:hidden}
body{background:var(--bg);font-family:"Open Sans",Arial,sans-serif;color:var(--ink);position:relative}
.label{position:absolute;font-size:17px;font-weight:600;color:var(--label)}
.sheet{position:absolute;background:var(--paper);box-shadow:0 3px 10px rgba(0,0,0,.18);overflow:hidden}
.wordmark{font-weight:400;color:var(--brand-blue);letter-spacing:.5px;line-height:1}
.tagline{font-size:8px;color:var(--ink-soft);letter-spacing:.6px;margin-top:3px}
.centre{position:absolute;left:0;right:0;text-align:center}
.footer-lines{font-size:6.5px;color:var(--ink-soft);line-height:1.6}

/* letterheads */
.letterhead{top:70px;width:345px;height:444px}
.letterhead .logo-block{position:absolute;top:26px;right:26px;text-align:left}
.letterhead .wordmark{font-size:24px}
.letterhead .footer-lines{bottom:30px}
.letterhead--two .base-band{position:absolute;left:0;right:0;bottom:0;height:14px;background:var(--brand-blue)}
.letterhead--two .footer-lines{bottom:24px}

/* business cards */
.card{left:853px;width:232px;height:134px;border-radius:8px}
.card .logo-block{position:absolute;left:24px;top:22px}
.card .wordmark{font-size:26px}
.card--white .person{position:absolute;left:0;right:0;top:78px;text-align:center;font-size:9px;font-weight:600;color:var(--brand-blue)}
.card--white .role{font-size:6.5px;font-weight:400;color:var(--ink-soft)}
.card--white .footer-lines{bottom:10px;font-size:5.5px}
.card--dark{top:186px;background:linear-gradient(160deg,var(--charcoal),var(--charcoal-dark))}
.card--dark .wordmark{color:#fff}
.card--dark .tagline{color:#c9ccd1}
.card--dark .web{position:absolute;bottom:14px;left:0;right:0;text-align:center;font-size:7px;color:#c9ccd1}
.card--blue{top:356px;background:linear-gradient(160deg,var(--brand-blue-light),var(--brand-blue))}
.card--blue .wordmark{color:#fff}
.card--blue .tagline{color:#e3eefa}

/* reports */
.report{top:542px;height:453px}
.report .wordmark{font-size:38px}
.report .title{font-size:14px;font-weight:300;letter-spacing:1px}
.report .subtitle{font-size:9px;letter-spacing:1px;margin-top:3px}
.report .date{font-size:6.5px;margin-top:8px}
.report--cover-one{left:28px;width:353px;background:linear-gradient(180deg,#f2f4f7 0%,#ffffff 55%)}
.report--cover-one .logo-block{position:absolute;left:30px;top:160px}
.report--cover-one .accent-stripe{position:absolute;left:0;right:0;top:282px;height:10px;background:var(--brand-blue-light);opacity:.5}
.report--cover-one .title-band{position:absolute;left:0;right:0;top:292px;bottom:0;background:var(--brand-blue);color:#fff;text-align:center;padding-top:52px}
.report--cover-two{left:431px;width:342px;background:linear-gradient(180deg,#eef1f5 0%,#ffffff 50%)}
.report--cover-two .logo-block{position:absolute;left:60px;top:120px}
.report--cover-two .title-block{top:305px;color:var(--ink)}
.report--cover-two .base-band{position:absolute;left:0;right:0;bottom:0;height:12px;background:var(--brand-blue)}
.report--inner{left:828px;width:340px}
.report--inner .logo-block{position:absolute;right:18px;top:16px}
.report--inner .wordmark{font-size:14px}
.report--inner .tagline{font-size:5px;margin-top:1px}
.report--inner .page-band{position:absolute;left:0;right:0;bottom:0;height:14px;background:var(--brand-blue);color:#fff;font-size:6px;text-align:right;padding:3px 14px 0 0}
.report--inner .top-rule{position:absolute;left:18px;right:18px;top:52px;height:1px;background:#d6dbe1}
</style>
</head>
<body>

<div class="label" style="left:118px;top:38px">Option 1</div>
<div class="label" style="left:505px;top:38px">Option 2</div>
<div class="label" style="left:1110px;top:242px">Option 1</div>
<div class="label" style="left:1110px;top:413px">Option 2</div>
<div class="label" style="left:90px;top:516px">Report Cover Option 1</div>
<div class="label" style="left:490px;top:516px">Report Cover Option 2</div>
<div class="label" style="left:895px;top:516px">Report Cover (INNER PAGE)</div>

<section class="sheet letterhead letterhead--one" style="left:28px">
  <div class="logo-block"><div class="wordmark">lumenvex</div><div class="tagline">research &amp; consulting</div></div>
  <div class="centre footer-lines">
    Level 1, 57 Pemberly Road, Milford, Auckland &nbsp;|&nbsp; PO Box 46-582, Auckland 0963<br>
    Ph +64 9 555 0142 &nbsp;|&nbsp; rosalind@lumenvex.co.nz<br>
    www.lumenvex.co.nz
  </div>
</section>

<section class="sheet letterhead letterhead--two" style="left:395px;width:372px">
  <div class="logo-block"><div class="wordmark">lumenvex</div><div class="tagline">research &amp; consulting</div></div>
  <div class="centre footer-lines">
    Level 1, 57 Pemberly Road, Milford, Auckland &nbsp;|&nbsp; PO Box 46-582, Auckland 0963<br>
    Ph +64 9 555 0142 &nbsp;|&nbsp; rosalind@lumenvex.co.nz
  </div>
  <div class="base-band"></div>
</section>

<section class="sheet card card--white" style="top:33px">
  <div class="logo-block"><div class="wordmark">lumenvex</div><div class="tagline">research &amp; consulting</div></div>
  <div class="person">Rosalind Thorpe<br><span class="role">Director</span></div>
  <div class="centre footer-lines">
    Level 1, 57 Pemberly Road, Milford, Auckland &nbsp; PO Box 46-582, Auckland 0963<br>
    M +64 21 555 0187 &nbsp; rosalind@lumenvex.co.nz
  </div>
</section>

<section class="sheet card card--dark">
  <div class="logo-block"><div class="wordmark">lumenvex</div><div class="tagline">research &amp; consulting</div></div>
  <div class="web">www.lumenvex.co.nz</div>
</section>

<section class="sheet card card--blue">
  <div class="logo-block"><div class="wordmark">lumenvex</div><div class="tagline">research &amp; consulting</div></div>
</section>

<section class="sheet report report--cover-one">
  <div class="logo-block"><div class="wordmark">lumenvex</div><div class="tagline">research &amp; consulting</div></div>
  <div class="accent-stripe"></div>
  <div class="title-band">
    <div class="title">BRAND RESEARCH RESULTS</div>
    <div class="subtitle">ABC COMPANY</div>
    <div class="date">March 2012</div>
  </div>
</section>

<section class="sheet report report--cover-two">
  <div class="logo-block"><div class="wordmark">lumenvex</div><div class="tagline">research &amp; consulting</div></div>
  <div class="centre title-block">
    <div class="title">BRAND RESEARCH RESULTS</div>
    <div class="subtitle">ABC COMPANY</div>
    <div class="date">March 2012</div>
  </div>
  <div class="base-band"></div>
</section>

<section class="sheet report report--inner">
  <div class="logo-block"><div class="wordmark">lumenvex</div><div class="tagline">research &amp; consulting</div></div>
  <div class="top-rule"></div>
  <div class="page-band">Page 1</div>
</section>

</body>
</html>
```